Modern Business Card

Modern professional business card with more than just logo and demographic info. Something memorable.

We are a trendy/modern chiropractic group with an emphasis on neurology, hence the minimalist-type brain logo. We want to convey that modern and technical aspect with professionalism and the elite nature of our practice environment.

```html
<!DOCTYPE html>
<html lang="en">
<head>
<meta charset="UTF-8">
<title>Keystone Spine – Business Card</title>
<link rel="stylesheet" href="https://fonts.googleapis.com/css2?family=Cinzel:wght@500&family=Montserrat:wght@400;500&display=swap">
<style>
  :root {
    --page-bg: #2a2a2c;
    --brand-blue: #4a7fc1;
    --brand-blue-deep: #3f74bb;
    --brand-blue-light: #4f89cf;
    --card-white: #ffffff;
    --text-grey: #4a4a4a;
  }
  * { margin: 0; padding: 0; box-sizing: border-box; }
  html, body { width: 1200px; height: 900px; overflow: hidden; }
  body {
    background: var(--page-bg);
    position: relative;
    font-family: "Montserrat", sans-serif;
  }
  .card {
    position: absolute;
    left: 280px;
    width: 640px;
    height: 366px;
    border-radius: 18px;
    overflow: hidden;
  }
  /* Back side */
  .card-back { top: 60px; }
  .back-pattern {
    position: absolute; inset: 0;
    background: linear-gradient(100deg, var(--brand-blue-deep), var(--brand-blue) 55%, var(--brand-blue-light));
  }
  .back-wordmark {
    position: absolute;
    right: 52px; bottom: 52px;
    font-family: "Cinzel", serif;
    font-weight: 500;
    color: var(--card-white);
    line-height: 0.95;
    text-align: left;
  }
  .back-wordmark .word-main { display: block; font-size: 30px; letter-spacing: 1px; }
  .back-wordmark .word-sub { display: block; font-size: 15px; letter-spacing: 1px; }

  /* Front side */
  .card-front { top: 474px; background: var(--card-white); }
  .name-accent {
    position: absolute; left: 0; top: 34px;
    width: 9px; height: 42px;
    background: var(--brand-blue);
  }
  .holder-name {
    position: absolute; left: 36px; top: 32px;
    font-family: "Cinzel", serif; font-weight: 500;
    font-size: 24px; color: var(--brand-blue); letter-spacing: 0.5px;
  }
  .holder-role {
    position: absolute; left: 36px; top: 64px;
    font-size: 15px; color: var(--text-grey); letter-spacing: 0.5px;
  }
  .front-wordmark {
    position: absolute; right: 40px; top: 108px;
    font-family: "Cinzel", serif; font-weight: 500;
    color: var(--brand-blue); line-height: 0.9;
  }
  .front-wordmark .word-main { display: block; font-size: 54px; letter-spacing: 1px; }
  .front-wordmark .word-sub { display: block; font-size: 28px; letter-spacing: 1px; }
  .address {
    position: absolute; left: 36px; top: 196px;
    font-size: 17px; line-height: 1.35; color: var(--text-grey); letter-spacing: 0.5px;
  }
  .contact-band {
    position: absolute; left: 0; top: 252px;
    width: 530px; height: 94px;
    background: var(--brand-blue);
  }
  .contact-list {
    position: absolute; left: 22px; top: 10px;
    list-style: none;
  }
  .contact-list li {
    display: flex; align-items: center; gap: 12px;
    height: 25px;
    font-size: 16px; color: var(--card-white); letter-spacing: 0.5px;
  }
  .contact-list svg { width: 14px; height: 14px; flex: none; }
</style>
</head>
<body>
  <section class="card card-back">
    <div class="back-pattern" role="img" aria-label="Repeating pattern of brain motifs in lighter blue"></div>
    <div class="back-wordmark">
      <span class="word-main">KEYSTONE</span>
      <span class="word-sub">SPINE</span>
    </div>
  </section>

  <section class="card card-front">
    <div class="name-accent"></div>
    <h1 class="holder-name">DANIEL MERCER</h1>
    <p class="holder-role">Director</p>

    <div class="front-wordmark">
      <span class="word-main">KEYSTONE</span>
      <span class="word-sub">SPINE</span>
    </div>

    <p class="address">1187 Linden Ridge<br>Salem, OR 97301</p>

    <div class="contact-band">
      <ul class="contact-list">
        <li>
          <svg viewBox="0 0 16 16" aria-hidden="true"><path d="M4 1.5 L6 5 L4.6 6.4 C5.5 8.4 7.6 10.5 9.6 11.4 L11 10 L14.5 12 L13 14.5 C7 14.5 1.5 9 1.5 3 Z" fill="#fff"/></svg>
          (555) 014-2286
        </li>
        <li>
          <svg viewBox="0 0 16 16" aria-hidden="true"><rect x="1.5" y="3.5" width="13" height="9" fill="none" stroke="#fff" stroke-width="1.4"/><path d="M1.5 3.5 L8 9 L14.5 3.5" fill="none" stroke="#fff" stroke-width="1.4"/></svg>
          hello@keystonespine.com
        </li>
        <li>
          <svg viewBox="0 0 16 16" aria-hidden="true"><circle cx="8" cy="8" r="6.5" fill="none" stroke="#fff" stroke-width="1.3"/><ellipse cx="8" cy="8" rx="3" ry="6.5" fill="none" stroke="#fff" stroke-width="1.1"/><path d="M1.5 8 H14.5 M2.5 5 H13.5 M2.5 11 H13.5" stroke="#fff" stroke-width="1"/></svg>
          www.keystonespine.com
        </li>
      </ul>
    </div>
  </section>
</body>
</html>
```